Label for Gin Bottle - Cranberry & Peach

Hi, We have created a Cranberry & Peach Gin that we require a label for.
The gin will be a vivid Orange/red colour in a clear 50cl bottle
The gin will be 40% Vol.
I am looking for a classy design with a summer/fresh appearance.
Thank You.

```html
<!DOCTYPE html>
<html lang="en">
<head>
<meta charset="utf-8">
<title>Cranberry &amp; Peach Gin Label</title>
<link rel="stylesheet" href="https://fonts.googleapis.com/css2?family=Cardo&family=Roboto+Condensed:wght@300&display=swap">
<style>
  :root {
    --ink: #58595b;
    --frame: #a7a9ac;
    --paper: #ffffff;
    --cranberry: #e21c44;
    --peach: #f5a07c;
    --peach-deep: #f1764f;
    --leaf: #abd8a6;
  }
  html, body {
    margin: 0;
    padding: 0;
    width: 909px;
    height: 1200px;
    overflow: hidden;
    background: var(--paper);
  }
  .label {
    position: relative;
    width: 909px;
    height: 1200px;
    background: var(--paper);
    box-sizing: border-box;
    border: 7px solid var(--frame);
    border-radius: 44px;
  }
  .label__inner-frame {
    position: absolute;
    inset: 11px;
    border: 2px solid var(--frame);
    border-radius: 34px;
  }
  .title {
    position: absolute;
    left: 0;
    right: 0;
    top: 236px;
    margin: 0;
    text-align: center;
    font-family: "Cardo", serif;
    font-weight: 400;
    font-size: 104px;
    line-height: 108px;
    color: var(--ink);
  }
  .title__line {
    display: block;
  }
  .fruit-art {
    position: absolute;
    left: 180px;
    top: 544px;
    width: 546px;
    height: 214px;
    border-radius: 107px;
    background: linear-gradient(90deg, var(--leaf) 0%, var(--cranberry) 22%, var(--peach) 50%, var(--peach-deep) 75%, var(--cranberry) 88%, var(--leaf) 100%);
  }
  .spirit {
    position: absolute;
    left: 0;
    right: 0;
    top: 828px;
    margin: 0;
    text-align: center;
    font-family: "Cardo", serif;
    font-weight: 400;
    font-size: 150px;
    letter-spacing: 42px;
    padding-left: 42px;
    color: var(--ink);
    line-height: 1;
  }
  .spec {
    position: absolute;
    top: 1092px;
    margin: 0;
    font-family: "Roboto Condensed", sans-serif;
    font-weight: 300;
    font-size: 52px;
    color: var(--ink);
    line-height: 1;
  }
  .spec--abv { left: 60px; }
  .spec--volume { right: 76px; }
</style>
</head>
<body>
  <div class="label">
    <div class="label__inner-frame"></div>
    <h1 class="title">
      <span class="title__line">Cranberry</span>
      <span class="title__line">&amp; Peach</span>
    </h1>
    <div class="fruit-art" role="img" aria-label="Illustration of cranberries, a halved peach and green leaves"></div>
    <p class="spirit">GIN</p>
    <p class="spec spec--abv">40% Vol</p>
    <p class="spec spec--volume">50cl</p>
  </div>
</body>
</html>
```